New product brochure for CEO's

We have created a research product that creates a syndicate of the CEO's from Australia's top 30 insurance firms. The purpose of the study is to ask CEO's to share their views on the future of the industry over the next 12 months.

The purpose of this flyer will be to email to CEO's an overview of the product prior to our company calling them to arrange a meeting. The purpose of the flyer will be to professionally and succintly lay out the concept and logistics of the new product.

Because CEO's are very time poor and often demanding people, we need a design that is simple but professional in appearance. From a design perspective, we naturally want the flyer to contain elements that reflect our company's master brand. We have included in the attachments copies of our company logo and business card. Please use these two elements to inspire your designs.

We want a clean design that does not contain any photographs or graphical images beyond any elements inspired by our company livery. The product is called the 'Boardroom Sector Compass'. Ideally, the flyer would create a design for this title that reflects our 'ravel' brand, in particular the use of the 'double helix' that appears to the left hand side of the ravel brand name in our logo.

For your reference, our company RGB colours are:

Logo:
Grey- #6d6e70 (RGB – 109,110,112)
Green - #8cc63e (RGB – 140,198,62)
Blue - #1b75bb (RGB – 27,117,187)
Font - Helvetica Neue Bold

Word:
Font – Calibri
Size – 10
Line Spacing: 1.15 (Multiple)
Between Paragraphs: 8pt (After)

We require a double sided flyer. We have included a word document that reflects the amount of text that will need to be contained on both the front and reverse side of the flyer.

The second side of the flyer will contain a list of the products deliverables. In the word document that we have provided, we have represented this as a series of bullet points. Please feel free to use your creative flair to display this information in other formats. For example - tables or shaded areas, etc.

In your designs please consider that the target market (namely CEO's) are typically male businessmen aged over 50 years. So whilst we are looking for a contemporary and modern design, it must not alienate an older target audience.

Project Deadline Extended Reason: Sorry, but we have had a major client ask us to undertake some urgent work. We apologise for the delay in providing feedback that this has caused. We expect to have a session first thing Tuesday morning to review the current designs. To be fair to those designers who are currently waiting on feedback we have extended the project by 5 days.Thank you for your understanding. Added Sunday, March 12, 2017

Target Market(s)

CEO's of large insurance firms

Industry/Entity Type

Insurance

Font styles to use
Other font styles liked:
• Refer to main brief

Requirements
Must have
• - Must use our company colours (see above in description)
• - Must be clean, simple and professional
• - Must incorporate our logo
• - Must create a logo / graphical treatment for the product name 'Boardroom Sector Compass'
• - Must provide sufficient space for text to be inserted within the document (as per attached example PDF file)
Should not have
• - Must not have any photographs

```html
<!DOCTYPE html>
<html lang="en">
<head>
<meta charset="utf-8">
<title>Boardroom Sector Compass – Flyer</title>
<link rel="stylesheet" href="https://fonts.googleapis.com/css2?family=Oswald:wght@500;600&family=Open+Sans:wght@400;700&family=Raleway:wght@500&display=swap">
<style>
  :root{
    --brand-grey:#6d6e70;
    --brand-green:#8cc63e;
    --brand-blue:#1b75bb;
    --blue-light:#3d92d8;
    --paper:#f6f7f8;
    --panel:#e7e8ea;
    --stage:#e4e5e7;
    --white:#ffffff;
    --body-on-grey:#f1f1f1;
    --body-on-white:#7a7b7e;
    --rule:#d4dbe3;
  }
  *{box-sizing:border-box;margin:0;padding:0}
  html,body{width:1200px;height:910px;overflow:hidden;background:var(--stage)}
  body{position:relative;font-family:"Open Sans",Arial,sans-serif}

  .page{position:absolute;top:38px;width:552px;height:781px;background:var(--paper);overflow:hidden;box-shadow:0 2px 10px rgba(0,0,0,.18)}
  .page--front{left:30px}
  .page--back{left:618px}
  .page__shapes{position:absolute;inset:0}
  .abs{position:absolute}

  /* wordmark */
  .wordmark{display:flex;align-items:center;gap:10px;color:var(--brand-grey);font-family:"Open Sans",Arial,sans-serif;font-weight:700;letter-spacing:-2px;line-height:1}
  .wordmark__dot{width:26px;height:26px;border-radius:50%;background:var(--brand-blue)}
  .wordmark--front{left:360px;top:24px;font-size:58px}
  .wordmark--back{left:200px;top:612px;font-size:64px}
  .wordmark--back .wordmark__dot{width:28px;height:28px}

  /* front title */
  .cover-title{right:22px;top:156px;text-align:right;font-family:"Oswald",Impact,sans-serif;font-weight:600;font-size:42px;line-height:1.12;color:var(--white);text-transform:uppercase}
  .cover-title__accent{color:var(--brand-green)}
  .cover-title__rule{right:22px;top:307px;width:104px;height:1px;background:var(--white)}
  .cover-tagline{right:22px;top:312px;text-align:right;font-family:"Raleway",Arial,sans-serif;font-weight:500;font-size:18px;line-height:1.3;color:var(--white)}

  .photo{left:0;top:0;width:552px;height:781px}

  /* sections */
  .section__heading{font-family:"Oswald",Impact,sans-serif;font-weight:500;font-size:14px;letter-spacing:.2px;text-transform:uppercase;margin-bottom:5px}
  .section__body p{font-size:7.6px;line-height:1.55;margin-bottom:6px;text-align:justify}
  .section--dark .section__heading{color:var(--brand-green)}
  .section--dark .section__body p{color:var(--body-on-grey)}
  .section--light .section__heading{color:var(--brand-blue)}
  .section--light .section__body p{color:var(--body-on-white)}
  .section--concept{left:58px;top:414px;width:190px}
  .section--benefits{left:58px;top:534px;width:190px}
  .section--process{left:334px;top:426px;width:190px}
  .section--investment{left:334px;top:604px;width:190px}

  .icon{position:absolute;width:34px;height:34px;border-radius:50%;display:flex;align-items:center;justify-content:center}
  .icon--light{background:var(--white)}
  .icon--blue{background:var(--brand-blue)}

  .site-url{left:346px;top:750px;font-size:13px;letter-spacing:2px;color:var(--white)}

  /* back */
  .product-title{left:80px;top:80px;width:392px;height:58px;border:1.5px solid var(--blue-light);border-radius:6px;background:var(--white);display:flex;align-items:center;justify-content:center;font-family:"Oswald",Impact,sans-serif;font-weight:500;font-size:27px;white-space:nowrap;color:var(--brand-blue);text-transform:uppercase;letter-spacing:.2px}
  .metric-tab{display:flex;align-items:center;justify-content:center;background:var(--blue-light);color:var(--white);font-family:"Oswald",Impact,sans-serif;font-weight:500;font-size:20px;letter-spacing:1px;text-transform:uppercase}
  .metric-tab span{white-space:nowrap}
  .metric-tab--core{left:0;top:166px;width:58px;height:203px}
  .metric-tab--core span{transform:rotate(-90deg)}
  .metric-tab--seasonal{left:504px;top:397px;width:48px;height:191px}
  .metric-tab--seasonal span{transform:rotate(90deg)}
  .panel--core{left:58px;top:166px;width:494px;height:203px;background:var(--panel)}
  .panel--seasonal{left:0;top:389px;width:504px;height:199px;background:var(--white)}

  .metric-list{list-style:none}
  .metric-list li{display:flex;align-items:center;gap:10px;color:var(--brand-blue);font-weight:700;text-transform:uppercase;border-bottom:1px solid var(--rule);white-space:nowrap}
  .metric-list li::before{content:"";flex:none;width:8px;height:8px;border-radius:50%;background:var(--brand-blue)}
  .metric-list--core{left:70px;top:174px;width:320px}
  .metric-list--core li{font-size:7.6px;height:18.9px}
  .metric-list--seasonal{top:397px;width:226px}
  .metric-list--seasonal li{font-size:6.5px;height:18.9px;gap:8px}
  .metric-list--seasonal li::before{width:7px;height:7px}
  .metric-list--col-a{left:26px}
  .metric-list--col-b{left:262px}

  .contact-bar{left:0;top:713px;width:552px;height:68px;background:var(--brand-blue);display:flex;align-items:center;justify-content:center;color:var(--white);font-weight:700;font-size:15px;text-transform:uppercase;letter-spacing:.2px}
</style>
</head>
<body>

<section class="page page--front" aria-label="Flyer front">
  <svg class="page__shapes" width="552" height="781" viewBox="0 0 552 781">
    <polygon points="0,0 300,0 0,62" fill="var(--blue-light)"/>
    <polygon points="0,0 190,0 0,38" fill="var(--brand-blue)"/>
    <polygon points="0,60 552,132 552,146 0,78" fill="var(--brand-grey)"/>
    <polygon points="0,78 552,146 552,152 0,93" fill="var(--brand-blue)"/>
  </svg>

  <div class="abs photo" role="img" aria-label="Photograph of a businessman in a suit looking out over a city skyline"
       style="clip-path:polygon(0 93px,552px 152px,552px 400px,0 370px);background:linear-gradient(180deg,#f4f5f6 0%,#dfe2e6 55%,#8f9499 80%,#5f6367 100%)"></div>

  <svg class="page__shapes" width="552" height="781" viewBox="0 0 552 781">
    <polygon points="346,136 552,152 552,400 258,380" fill="var(--brand-grey)" opacity=".88"/>
    <polygon points="0,368 272,382 272,781 0,781" fill="var(--brand-grey)"/>
    <polygon points="272,376 552,398 552,432 272,402" fill="var(--brand-blue)"/>
    <polygon points="272,402 552,432 552,781 272,781" fill="var(--white)"/>
    <polygon points="330,746 552,746 552,769 322,769" fill="var(--brand-blue)"/>
    <g stroke="var(--white)" stroke-width="1" fill="none">
      <polyline points="54,422 33,422 33,470"/>
      <polyline points="54,542 33,542 33,662"/>
    </g>
    <g stroke="var(--brand-blue)" stroke-width="1" fill="none">
      <polyline points="330,434 306,434 306,497"/>
      <polyline points="330,612 306,612 306,637"/>
    </g>
  </svg>

  <div class="abs wordmark wordmark--front"><span class="wordmark__dot"></span>ravel</div>

  <h1 class="abs cover-title">Boardroom<br>Sector<br><span class="cover-title__accent">Compass</span></h1>
  <div class="abs cover-title__rule"></div>
  <p class="abs cover-tagline">ravel is a next generation<br>market research firm.</p>

  <div class="icon icon--light" style="left:16px;top:470px">
    <svg width="18" height="18" viewBox="0 0 18 18"><path d="M9 2a5 5 0 0 0-3 9v2h6v-2a5 5 0 0 0-3-9z" fill="none" stroke="var(--brand-grey)" stroke-width="1.5"/><rect x="6.5" y="14" width="5" height="2" fill="var(--brand-grey)"/></svg>
  </div>
  <div class="icon icon--light" style="left:16px;top:662px">
    <svg width="18" height="18" viewBox="0 0 18 18"><polyline points="2,15 2,2" stroke="var(--brand-grey)" stroke-width="1.5"/><polyline points="2,15 16,15" stroke="var(--brand-grey)" stroke-width="1.5"/><polyline points="4,12 8,7 11,10 15,4" fill="none" stroke="var(--brand-grey)" stroke-width="1.5"/></svg>
  </div>
  <div class="icon icon--blue" style="left:289px;top:497px">
    <svg width="18" height="18" viewBox="0 0 18 18" fill="none" stroke="var(--white)" stroke-width="1.6"><path d="M3 8a6 6 0 0 1 11-3"/><polyline points="14,1 14,5 10,5"/><path d="M15 10a6 6 0 0 1-11 3"/><polyline points="4,17 4,13 8,13"/></svg>
  </div>
  <div class="icon icon--blue" style="left:289px;top:637px">
    <svg width="18" height="18" viewBox="0 0 18 18"><circle cx="9" cy="9" r="7" fill="none" stroke="var(--white)" stroke-width="1.4"/><text x="9" y="13" text-anchor="middle" font-family="Open Sans,Arial,sans-serif" font-weight="700" font-size="11" fill="var(--white)">$</text></svg>
  </div>

  <div class="abs section section--dark section--concept">
    <h2 class="section__heading">Concept</h2>
    <div class="section__body">
      <p>Each quarter we gather the chief executives of Australia's top thirty insurers to share a confidential view of where the industry is heading over the next twelve months.</p>
    </div>
  </div>

  <div class="abs section section--dark section--benefits">
    <h2 class="section__heading">Benefits</h2>
    <div class="section__body">
      <p>Gain a clear read on peer sentiment before it reaches the market. Benchmark your own strategy against the collective outlook of the sector's most senior leaders in one concise report.</p>
      <p>Spend less time on research and more time on decisions. Each briefing is short, structured and built for leaders who have only minutes to spare between board commitments.</p>
      <p>Join a trusted, invitation-only forum. All responses stay anonymous and are reported in aggregate, so every participant can speak openly about risks, pricing and growth.</p>
    </div>
  </div>

  <div class="abs section section--light section--process">
    <h2 class="section__heading">Process</h2>
    <div class="section__body">
      <p>A short interview is held with each chief executive every quarter. Questions cover market conditions, capital, regulation, claims trends and the talent agenda for the year ahead.</p>
      <p>Our analysts combine the responses into a single sector view, highlighting where leaders agree, where they differ and which signals deserve the closest attention.</p>
    </div>
  </div>

  <div class="abs section section--light section--investment">
    <h2 class="section__heading">Investment</h2>
    <div class="section__body">
      <p>Membership is offered as an annual subscription covering four quarterly briefings, a full year-end report and a private results session with our senior research team.</p>
    </div>
  </div>

  <p class="abs site-url">www.ravelresearch.com.au</p>
</section>

<section class="page page--back" aria-label="Flyer back">
  <svg class="page__shapes" width="552" height="781" viewBox="0 0 552 781">
    <polygon points="0,0 190,0 0,82" fill="var(--blue-light)"/>
    <polygon points="0,0 110,0 0,46" fill="var(--brand-blue)"/>
    <polygon points="362,0 552,0 552,82" fill="var(--blue-light)"/>
    <polygon points="442,0 552,0 552,46" fill="var(--brand-blue)"/>
  </svg>

  <div class="abs product-title">Boardroom Sector Compass</div>

  <div class="abs panel--core"></div>
  <div class="abs metric-tab metric-tab--core"><span>Core Metrics</span></div>
  <ul class="abs metric-list metric-list--core">
    <li>Twelve-month outlook for gross written premium growth</li>
    <li>Expected change in claims frequency and severity</li>
    <li>Confidence in current capital and reserve positions</li>
    <li>Priority investments in technology and data capability</li>
    <li>Views on regulatory change and compliance burden</li>
    <li>Pricing pressure across personal and commercial lines</li>
    <li>Distribution shifts between brokers and direct channels</li>
    <li>Workforce, talent and leadership succession outlook</li>
    <li>Exposure to catastrophe and climate-related risk</li>
    <li>Appetite for mergers, acquisitions and partnerships</li>
  </ul>

  <div class="abs panel--seasonal"></div>
  <div class="abs metric-tab metric-tab--seasonal"><span>Seasonal Metrics</span></div>
  <ul class="abs metric-list metric-list--seasonal metric-list--col-a">
    <li>Quarterly shift in market confidence index</li>
    <li>Summer storm season claims expectations</li>
    <li>End of financial year renewal trends</li>
    <li>Reinsurance renewal pricing sentiment</li>
    <li>Winter motor claims outlook</li>
    <li>Bushfire season preparedness rating</li>
    <li>Quarterly customer retention outlook</li>
    <li>Half-year results expectations</li>
    <li>Budget and tax policy impact</li>
    <li>Interest rate and investment returns view</li>
  </ul>
  <ul class="abs metric-list metric-list--seasonal metric-list--col-b">
    <li>Quarterly hiring intentions</li>
    <li>Product launch plans for the quarter</li>
    <li>Flood risk and cover availability</li>
    <li>Broker commission trends by quarter</li>
    <li>Cyber claims activity outlook</li>
    <li>Marketing spend intentions</li>
    <li>Quarterly cost inflation pressures</li>
    <li>Peak season claims staffing needs</li>
    <li>Supplier and repairer capacity view</li>
    <li>Quarter-on-quarter sentiment change</li>
  </ul>

  <div class="abs wordmark wordmark--back"><span class="wordmark__dot"></span>ravel</div>

  <div class="abs contact-bar">Contact us at: info@ravelresearch.com.au</div>
</section>

</body>
</html>
```